New Design for Accounting Firm

CLIENT NAME: Corvanta
CURRENT WEBSITE: www.corvantagroup.example.com.au

CLIENTS THE CLIENT LIKES:
http://velduro.example.se/
http://www.layerport.example.biz/index.php
http://www.plinthworks.example.co.uk/
http://www.worldreliefmonitor.example.org/

COLOUR THEMES:
Colour theme to reflect the logo, with a leaning to blue in Accounting & Audit sections and green in Super section.

LOOK AND FEEL:
The look and feel needs to reflect an accessible culture and contemporary sensibility while still communicating our experience and stability as a professional company.

ABOUT:
The concept of 'Corvanta' is integral to our identity. Definition: 'The connection of creative ideas from a group of diverse individuals, applied with the end aim of solving practical problems'. See ''About Us'' on our website for more.

OTHER DETAILS:
Our three divisions (and service areas within each division) must be easily navigated as they related to very different users of the site. Two client sign in sections (Accounting & Super) must be easily distinguished to avoid user confusion.

MENU STRUCTURE:
* About
- includes history, values, our people, community etc
* Accounting & Advisory
- About
- Services
- Tax & Accounting
- Business Advisory
- Family Wealth Management
- Client Sign In
- Calculators
* Audit & Assurance
- About
- Services
* Corvanta Super
- About
- Individuals
- Services
- Advisers
- Services
- Portal Sign In
- Calculators
* Careers
* Newsletters
* Contact

REQUIREMENTS:
- Layered PSD form home and content pages
- No coding required, we use our own CMS to insert XHTML files into.
Updates

Hi Guys,

The client has asked for a non-cliche'd images in the design. If you'd like to try again with some images that represent the business but aren't your standard boring accounting-looking people, then please do! Cliche is a killer in design - please pump some creativity in!

Cheers,
Ned.

Reason: GUYS - PLEASE LISTEN TO THESE COMMENTS - I'VE SAID THEM TWICE NOW AND PEOPLE ARE STILL POSTING PROJECTS WITH CLICHED AND OBVIOUS ACCOUTNING TYPE IMAGES. USE YOUR CREATIVITY AND POST A DESIGN THAT IS OUTSIDE THE BOX WITH REGARDS TO THE IMAGES YOU ARE USING.

Reason: I am waiting to hear back from the client on their decision.

Industry/Entity Type

Accounting

```html
<!DOCTYPE html>
<html lang="en">
<head>
<meta charset="utf-8">
<title>Corvanta — Home</title>
<link rel="stylesheet" href="https://fonts.googleapis.com/css2?family=Noto+Sans:ital,wght@0,400;0,700;1,400&family=Fredoka:wght@400;500&family=Tinos:ital,wght@0,700;1,700&display=swap">
<style>
  :root{
    --frame-blue:#0f5ce6;
    --brand-blue:#1463e0;
    --nav-blue:#1565e8;
    --super-green:#62f232;
    --accent-orange:#f6a500;
    --login-orange:#f68a00;
    --login-dark:#3a2410;
    --news-orange:#f09a3c;
    --text-grey:#5c6b78;
    --link-blue:#1463d8;
    --quote-bg:#f3f6f6;
    --quote-title:#4c6078;
    --submit-grey:#7e8c8e;
    --white:#ffffff;
  }
  *{box-sizing:border-box;margin:0;padding:0}
  html,body{width:1200px;height:1200px;overflow:hidden}
  body{background:var(--frame-blue);font-family:"Noto Sans",sans-serif;position:relative}
  .page{position:absolute;left:50px;top:47px;width:1102px;height:1092px;background:var(--white)}
  .abs{position:absolute}

  .brand{left:84px;top:55px;width:224px;height:48px;display:flex;align-items:center;gap:10px;padding-left:22px;background:#f4f7fa;border-radius:6px;box-shadow:0 3px 5px rgba(0,0,0,.15)}
  .brand-mark{width:30px;height:30px;background:var(--brand-blue)}
  .brand-name{font-size:34px;color:var(--brand-blue);font-weight:400;letter-spacing:-.5px}

  .top-links{left:741px;top:64px;font-size:14.5px;color:var(--link-blue)}
  .top-links span{margin:0 6px}
  .enquiry{left:929px;top:64px;width:191px;height:30px;background:var(--accent-orange);color:var(--white);font-weight:700;font-size:17px;display:flex;align-items:center;justify-content:center;border-radius:3px;letter-spacing:.3px}

  .main-nav{left:84px;top:123px;height:28px;display:flex;background:var(--nav-blue)}
  .main-nav a{color:var(--white);text-decoration:none;font-weight:700;font-size:14px;display:flex;align-items:center;justify-content:center;border-right:1px solid #b9d0f6}
  .main-nav a:last-child{border-right:none}

  .panel{border-radius:4px}
  .panel-blue{left:87px;top:170px;width:679px;height:299px;background:var(--brand-blue)}
  .panel-green{left:780px;top:170px;width:338px;height:299px;background:var(--super-green)}
  .panel-title{font-family:"Fredoka",sans-serif;color:var(--white);font-size:26px;text-align:center;line-height:32px}
  .divider{left:435px;top:209px;width:1px;height:193px;background:#b8cdf3}
  .icon-box{border:2px solid var(--white);border-radius:8px;padding:4px}
  .icon-fill{width:100%;height:100%;border-radius:4px}
  .btn{display:flex;align-items:center;justify-content:center;color:var(--white);font-weight:700;font-size:18px;letter-spacing:.5px}

  .welcome-title{left:89px;top:488px;font-family:"Tinos",serif;font-weight:700;font-size:28px;color:var(--link-blue)}
  .welcome-rule{left:89px;top:520px;width:574px;height:1px;background:var(--super-green)}
  .welcome-body{left:91px;top:540px;width:650px;font-size:13.8px;line-height:21px;color:var(--text-grey)}
  .welcome-body p{margin-bottom:21px}
  .welcome-body ul{list-style:none;margin-bottom:21px}
  .welcome-body li{color:var(--link-blue)}
  .read-more{left:630px;top:1041px;font-family:"Tinos",serif;font-weight:700;font-size:14px;color:var(--link-blue)}
  .col-rule{left:762px;top:521px;width:1px;height:551px;background:#c9d3dc}

  .newsletter{left:784px;top:513px;width:331px;height:146px;background:var(--news-orange);border-radius:26px}
  .newsletter-title{left:0;top:8px;width:100%;text-align:center;font-family:"Tinos",serif;font-style:italic;font-weight:700;font-size:28px;color:#5b5668}
  .newsletter-input{left:48px;top:56px;width:239px;height:24px;background:var(--white);border:1px solid #6a6a6a}
  .newsletter-submit{left:113px;top:107px;width:107px;height:25px;background:var(--submit-grey);color:var(--white);font-weight:700;font-size:18px;display:flex;align-items:center;justify-content:center}

  .testimonials{left:789px;top:688px;width:319px;height:375px;background:var(--quote-bg);border-radius:6px;overflow:hidden}
  .testimonials-title{left:0;top:11px;width:100%;text-align:center;font-family:"Tinos",serif;font-weight:700;font-size:21px;color:var(--quote-title)}
  .testimonials-rule{left:28px;top:43px;width:267px;height:1px;background:var(--quote-title)}
  .testimonials-body{left:24px;top:61px;width:278px;font-size:13.8px;line-height:21px;color:var(--text-grey)}
  .testimonials-body p{margin-bottom:21px}

  .footer-rule{left:50px;top:1102px;width:1102px;height:2px;background:var(--brand-blue)}
  .footer-links{left:88px;top:1111px;font-size:10.5px;color:#8d98a2;letter-spacing:.1px}
  .footer-links span{margin:0 4px}
  .copyright{left:953px;top:1110px;font-size:10.5px;font-style:italic;color:var(--link-blue)}
</style>
</head>
<body>
  <div class="page"></div>

  <div class="abs brand"><div class="brand-mark"></div><span class="brand-name">Corvanta</span></div>
  <div class="abs top-links">Careers<span>I</span>Newsletters</div>
  <div class="abs enquiry">SEND AN ENQUIRY</div>

  <nav class="abs main-nav">
    <a style="width:86px">HOME</a>
    <a style="width:127px">WHO WE ARE</a>
    <a style="width:207px">ACCOUNTING &amp; ADVISORY</a>
    <a style="width:173px">AUDIT &amp; ASSURANCE</a>
    <a style="width:239px">SELF MANAGED SUPER FUNDS</a>
    <a style="width:78px">LINKS</a>
    <a style="width:124px">CONTACT US</a>
  </nav>

  <section class="abs panel panel-blue"></section>
  <div class="abs panel-title" style="left:110px;top:190px;width:300px">Accounting &amp; Advisory</div>
  <div class="abs panel-title" style="left:447px;top:192px;width:300px">Audit &amp; Assurance</div>
  <div class="abs divider"></div>
  <div class="abs icon-box" style="left:185px;top:251px;width:154px;height:124px">
    <div class="icon-fill" role="img" aria-label="Tax and report icon illustration" style="background:linear-gradient(160deg,#2a74ea,#1463e0)"></div>
  </div>
  <div class="abs icon-box" style="left:513px;top:254px;width:154px;height:125px">
    <div class="icon-fill" role="img" aria-label="Audit documents and dollar tick illustration" style="background:linear-gradient(160deg,#2a74ea,#1463e0)"></div>
  </div>
  <div class="abs btn" style="left:182px;top:400px;width:158px;height:39px;background:var(--login-orange)">CLIENT LOGIN</div>
  <div class="abs btn" style="left:510px;top:397px;width:158px;height:40px;background:var(--super-green)">KNOW MORE</div>

  <section class="abs panel panel-green"></section>
  <div class="abs panel-title" style="left:790px;top:180px;width:318px">Self Managed Super<br>Funds</div>
  <div class="abs icon-box" style="left:872px;top:252px;width:153px;height:124px">
    <div class="icon-fill" role="img" aria-label="Money bag with coin stacks illustration" style="background:radial-gradient(circle at 50% 55%,#e0892a,#7fe84a 75%)"></div>
  </div>
  <div class="abs btn" style="left:868px;top:396px;width:159px;height:40px;background:var(--login-dark)">CLIENT LOGIN</div>

  <h1 class="abs welcome-title">Welcome to Corvanta</h1>
  <div class="abs welcome-rule"></div>
  <div class="abs welcome-body">
    <p>Corvanta is a Tasmanian based firm which offers the skills of Accountants, Business Performace<br>Advisers, Auditors and Self Managed Super Fund Specialists.</p>
    <p>From our offices in Devonport and Hobart we deliver services across three divisions:</p>
    <ul>
      <li>&gt; AG Corvanta Chartered Accountants</li>
      <li>&gt; Corvanta Audit @ Assurance</li>
      <li>&gt; Corvanta Super</li>
    </ul>
    <p>Through our three divisions, our clients benefit from the application of specialist skills and systems,<br>developed in relevant areas of expertise.&nbsp; At the same time, our teams are skilled at integrating<br>their knowledge with the common goal of meeting our clients comprehensive needs.</p>
    <p>Across the firm we deliver services in a wide range of industries, to individuals, businesses,<br>corporations and financial advisers.</p>
    <p>Our services include:</p>
    <ul>
      <li>&gt; Accounting and Taxation</li>
      <li>&gt; Corporate and Business Advice</li>
      <li>&gt; Family Wealth Management</li>
      <li>&gt; Audit and Assurance</li>
      <li>&gt; Self Managed Super Fund Administration</li>
    </ul>
  </div>
  <div class="abs read-more">READ MORE....</div>
  <div class="abs col-rule"></div>

  <aside class="abs newsletter">
    <div class="abs newsletter-title">Join our Newsletter</div>
    <div class="abs newsletter-input"></div>
    <div class="abs newsletter-submit">SUBMIT</div>
  </aside>

  <aside class="abs testimonials">
    <div class="abs testimonials-title">Here what our users say!</div>
    <div class="abs testimonials-rule"></div>
    <div class="abs testimonials-body">
      <p>“Corvanta is a Tasmanian based firm which offers the skills of Accountants, Business Performace Advisers, Auditors and Self Managed Super Fund Specialists. Self Advisers, Auditors and Self Managed Super Fund Specialists. Performace Advisers, Auditors and Self Managed Super Fund Specialists. Performace Advisers, Auditors and Self Managed Super Fund Specialists.”</p>
      <p>- Liam Porter, Canada</p>
      <p>“Corvanta is a Tasmanian based firm which offers the skills of Accountants.”</p>
    </div>
  </aside>

  <div class="abs footer-rule"></div>
  <div class="abs footer-links">HOME<span>I</span>WHO WE ARE<span>I</span>ACCOUNTING &amp; ADVISORY<span>I</span>AUDIT &amp; ASSURANCE<span>I</span>SELF MANAGED SUPER FUNDS<span>I</span>LINKS<span>I</span>CONTACT US<span>I</span>CAREERS<span>I</span>NEWSLETTERS<span>I</span>PRIVACY</div>
  <div class="abs copyright">Copyright@2011 Corvanta Group</div>
</body>
</html>
```